Text design/overlay needed for promotional music release cover photo

I need the following text elements added to the attached image:
Element 1: Brent Colfax and The Kinship Circle
Element 2. This all needs to be clear and prominent : Featuring: Warren Petty, Corey Halvin, Renata Bloor, Ingrid Palumbo, Martin "Chipper" Lowe, Tamara Ridgely, Wa Ni Po Glen Harker, Nolan Brackett, Otis Crane, Dustin Pell, and The Final Grooveling
Element 3 ("WILLOW BEND" needs to pop): New single WILLOW BEND available everywhere 9/26
The final image needs to be 16:9 ratio. Colors should be black and samples from the bench in the image. Various fonts, text sizes, etc. The music is a reggae/bluegrass blend. I'm looking for art not AI. Thanks!

```html
<!DOCTYPE html>
<html lang="en">
<head>
<meta charset="utf-8">
<title>Brent Colfax and The Kinship Circle – Willow Bend</title>
<link rel="stylesheet" href="https://fonts.googleapis.com/css2?family=Bodoni+Moda:opsz,wght@6..96,600&family=Righteous&family=Montserrat:ital,wght@1,600;1,800&family=Kaushan+Script&family=Saira+Condensed:wght@300&family=Oswald:wght@500&display=swap">
<style>
  :root {
    --ink: #0b0b0b;
    --leaf-dark: #35591a;
    --leaf: #9cc23a;
    --ochre: #c9a23f;
    --rust: #b4533a;
    --clay: #6b2a1c;
    --band-green: #3d5e12;
    --paper: #ffffff;
    --gold: #f3b528;
    --amber: #e58a2a;
    --brick: #b5512f;
  }
  html, body {
    margin: 0;
    padding: 0;
    width: 1200px;
    height: 801px;
    overflow: hidden;
    background: var(--ink);
  }
  .release-cover {
    display: block;
    width: 1200px;
    height: 801px;
  }
  .artist-name {
    font-family: "Bodoni Moda", "Playfair Display", serif;
    font-weight: 600;
    fill: var(--ink);
  }
  .band-name {
    font-family: "Righteous", sans-serif;
    fill: var(--paper);
  }
  .single-label,
  .availability {
    font-family: "Montserrat", sans-serif;
    font-style: italic;
    fill: var(--ink);
  }
  .single-label { font-weight: 800; }
  .availability { font-weight: 600; }
  .single-title {
    font-family: "Kaushan Script", cursive;
    paint-order: stroke fill;
    stroke: var(--ink);
    stroke-width: 9;
    stroke-linejoin: round;
  }
  .release-date {
    font-family: "Saira Condensed", sans-serif;
    font-weight: 300;
    fill: none;
    stroke: var(--paper);
    stroke-width: 1;
  }
  .credits {
    font-family: "Oswald", sans-serif;
    font-weight: 500;
    fill: var(--paper);
    paint-order: stroke fill;
    stroke: #2a160f;
    stroke-width: 2.2;
    stroke-linejoin: round;
  }
</style>
</head>
<body>
<svg class="release-cover" viewBox="0 0 1200 801" xmlns="http://www.w3.org/2000/svg">
  <defs>
    <linearGradient id="backdrop" x1="0" y1="0" x2="0" y2="1">
      <stop offset="0" stop-color="var(--leaf-dark)"/>
      <stop offset="0.5" stop-color="#7a6a1f"/>
      <stop offset="1" stop-color="var(--clay)"/>
    </linearGradient>
    <linearGradient id="scene" x1="0" y1="0" x2="0" y2="1">
      <stop offset="0" stop-color="var(--leaf)"/>
      <stop offset="0.45" stop-color="var(--ochre)"/>
      <stop offset="1" stop-color="var(--rust)"/>
    </linearGradient>
    <linearGradient id="title-fill" x1="0" y1="0" x2="1" y2="0">
      <stop offset="0" stop-color="var(--gold)"/>
      <stop offset="0.55" stop-color="var(--amber)"/>
      <stop offset="1" stop-color="var(--brick)"/>
    </linearGradient>
  </defs>

  <rect class="backdrop" width="1200" height="801" fill="url(#backdrop)"/>

  <rect class="frame" x="39" y="75" width="1127" height="641" fill="var(--ink)"/>
  <rect class="cover-photo" x="52" y="87" width="1101" height="616" fill="url(#scene)"
        role="img" aria-label="Musician in cap and sunglasses seated on a colourful wooden bench on a dirt road through green woodland, electric guitar leaning beside him"/>

  <text class="artist-name" x="604" y="214" font-size="140" text-anchor="middle"
        textLength="810" lengthAdjust="spacingAndGlyphs">BRENT COLFAX</text>

  <rect class="band-plate" x="581" y="229" width="421" height="31" fill="var(--band-green)"/>
  <text class="band-name" x="791" y="254" font-size="24" text-anchor="middle"
        textLength="400" lengthAdjust="spacing">AND THE KINSHIP CIRCLE</text>

  <text class="single-label" x="792" y="337" font-size="26" text-anchor="middle"
        textLength="184" lengthAdjust="spacingAndGlyphs">NEW SINGLE</text>

  <text class="single-title" x="796" y="408" font-size="80" text-anchor="middle" fill="url(#title-fill)"
        textLength="390" lengthAdjust="spacingAndGlyphs">Willow Bend</text>

  <rect class="availability-plate" x="668" y="443" width="282" height="26" fill="rgba(255,255,255,0.55)" stroke="rgba(255,255,255,0.8)" stroke-width="1"/>
  <text class="availability" x="800" y="463" font-size="18" text-anchor="middle"
        textLength="248" lengthAdjust="spacingAndGlyphs">AVAILABLE EVERYWHERE</text>

  <text class="release-date" x="806" y="577" font-size="132" text-anchor="middle"
        textLength="212" lengthAdjust="spacingAndGlyphs">9/26</text>

  <text class="credits" font-size="14" text-anchor="middle">
    <tspan x="812" y="632" textLength="465" lengthAdjust="spacingAndGlyphs">FEATURING: WARREN PETTY, COREY HALVIN, RENATA BLOOR, INGRID PALUMBO,</tspan>
    <tspan x="812" y="651" textLength="450" lengthAdjust="spacingAndGlyphs">MARTIN “CHIPPER” LOWE, TAMARA RIDGELY, WA NI PO GLEN HARKER, NOLAN BRACKETT,</tspan>
    <tspan x="812" y="670" textLength="274" lengthAdjust="spacingAndGlyphs">OTIS CRANE, DUSTIN PELL, AND THE FINAL GROOVELING</tspan>
  </text>
</svg>
</body>
</html>
```